dsadasdasdasdsa

Industry/Entity Type

Mortgage Broking

Requirements
Must have
• Call-to-action button somewhere on the graphic
Nice to have
• The font of our logo is Montserrat

```html
<!DOCTYPE html>
<html lang="en">
<head>
<meta charset="utf-8">
<title>Mortgage Broker Directory Banner</title>
<link href="https://fonts.googleapis.com/css2?family=Montserrat:wght@500;600&display=swap" rel="stylesheet">
<style>
  :root {
    --backdrop: #4a4a4a;
    --paper: #ffffff;
    --green-top: #27a846;
    --green-bottom: #55bd4b;
    --green-dark: #187c44;
    --green-light: #7cc242;
    --ring-grey: #cfcfcf;
    --cta-maroon: #6b1e14;
    --text-light: #ffffff;
    --mascot-tone-a: #8fcf8f;
    --mascot-tone-b: #b98a62;
  }
  * { margin: 0; padding: 0; box-sizing: border-box; }
  html, body {
    width: 1200px;
    height: 1200px;
    overflow: hidden;
    background: var(--backdrop);
  }
  .banner {
    position: absolute;
    left: 60px;
    top: 526px;
    width: 1080px;
    height: 147px;
    background: linear-gradient(180deg, var(--green-top), var(--green-bottom));
    box-shadow: 0 4px 14px rgba(0, 0, 0, 0.55);
    overflow: hidden;
    font-family: "Montserrat", sans-serif;
  }
  .banner__shapes {
    position: absolute;
    inset: 0;
    width: 100%;
    height: 100%;
  }
  .mascot {
    position: absolute;
    bottom: 0;
    border-radius: 10px 10px 0 0;
    background: linear-gradient(180deg, var(--mascot-tone-a), var(--mascot-tone-b));
    opacity: 0.55;
  }
  .mascot--left {
    left: 0;
    top: 3px;
    width: 148px;
  }
  .mascot--right {
    left: 923px;
    top: 2px;
    width: 113px;
  }
  .banner__headline {
    position: absolute;
    left: 0;
    right: 0;
    top: 32px;
    text-align: center;
    color: var(--text-light);
    font-size: 32.5px;
    font-weight: 600;
    line-height: 38px;
    letter-spacing: 0.2px;
  }
  .banner__cta {
    position: absolute;
    left: 319px;
    top: 83px;
    width: 437px;
    height: 28px;
    background: var(--cta-maroon);
    border-radius: 4px;
    color: var(--text-light);
    font-size: 18.6px;
    font-weight: 500;
    line-height: 28px;
    text-align: center;
    text-decoration: none;
    white-space: nowrap;
  }
</style>
</head>
<body>
  <div class="banner">
    <svg class="banner__shapes" viewBox="0 0 1739 237" preserveAspectRatio="none" aria-hidden="true">
      <path d="M0 0 H335 C395 60 412 150 402 237 H0Z" fill="var(--green-dark)"/>
      <path d="M0 0 H275 C335 60 368 150 362 237 H0Z" fill="var(--green-light)"/>
      <path d="M0 0 H262 C320 60 342 150 334 237 H0Z" fill="var(--paper)"/>
      <path d="M0 0 H249 C305 60 332 150 324 237 H0Z" fill="var(--ring-grey)"/>
      <path d="M0 0 H234 C290 60 316 150 308 237 H0Z" fill="var(--paper)"/>
      <path d="M1739 0 H1319 C1285 70 1300 170 1374 237 H1739Z" fill="var(--green-dark)"/>
      <path d="M1739 0 H1359 C1332 70 1345 170 1404 237 H1739Z" fill="var(--green-light)"/>
      <path d="M1739 0 H1384 C1365 70 1395 170 1459 237 H1739Z" fill="var(--paper)"/>
      <path d="M1739 0 H1396 C1380 70 1410 170 1479 237 H1739Z" fill="var(--ring-grey)"/>
      <path d="M1739 0 H1411 C1396 70 1425 170 1494 237 H1739Z" fill="var(--paper)"/>
    </svg>

    <div class="mascot mascot--left" role="img" aria-label="Smiling cartoon turtle mascot, head and shoulders"></div>
    <div class="mascot mascot--right" role="img" aria-label="Cartoon turtle mascot standing and holding a small house"></div>

    <h1 class="banner__headline">Need a Mortgage Broker?</h1>
    <a class="banner__cta" href="#">Search Now on Australia's Largest Directory</a>
  </div>
</body>
</html>
```